For Lease sign for Property management company in Kansas City

We need someone to take our information and design a standard for lease sign that we can put in front of each of our buildings. I would love for it to do its job of letting people know there are units available but also be unique somehow. Also the aspect ratio of the design would ideally be 4 wide by 3 tall but we open to other ideas. It will be a larger yard sign.

Target Market(s)

Potential Tenants

Industry/Entity Type

Real Estate Development

Font styles to use
Sans Serif

Requirements
Must have
• Our logo, our website (www.quillstead-properties.com), our phone number (816) 555-2719.
Nice to have
• Some how say "For Lease"
Sign to be 4' wide by 3' tall
If there was a place to put the building name that would be cool but not ne
Should not have
• Nothing that I can think of

```html
<!DOCTYPE html>
<html lang="en">
<head>
<meta charset="utf-8">
<title>For Lease – Quillstead Properties</title>
<link rel="stylesheet" href="https://fonts.googleapis.com/css2?family=Bangers&family=Barlow:wght@500;700&family=Barlow+Condensed:wght@700&display=swap">
<style>
  :root {
    --amber: #d99a3a;
    --signal-red: #c01f2f;
    --white: #ffffff;
    --ink: #3a3b3d;
    --muted: #5a5b5e;
  }
  html, body {
    margin: 0;
    padding: 0;
    width: 1200px;
    height: 900px;
    overflow: hidden;
    background: var(--white);
  }
  .lease-sign {
    position: relative;
    width: 1200px;
    height: 900px;
    background: var(--white);
  }
  .sign-field {
    position: absolute;
    inset: 0 0 auto 0;
    height: 698px;
    background: var(--amber);
    overflow: hidden;
  }
  .headline-art {
    position: absolute;
    inset: 0;
    width: 1200px;
    height: 698px;
  }
  .headline-text {
    font-family: "Bangers", "Arial Black", sans-serif;
    fill: var(--white);
  }
  .building-plate {
    position: absolute;
    left: 82px;
    top: 490px;
    width: 1037px;
    height: 163px;
    background: var(--white);
    border-radius: 26px;
    display: flex;
    align-items: center;
    justify-content: center;
    font-family: "Barlow", sans-serif;
    font-weight: 500;
    font-size: 86px;
    color: var(--ink);
    letter-spacing: 0.5px;
  }
  .brand {
    position: absolute;
    left: 66px;
    top: 738px;
    display: flex;
    align-items: center;
    gap: 18px;
  }
  .brand-dot {
    width: 96px;
    height: 96px;
    border-radius: 50%;
    background: var(--amber);
  }
  .brand-name {
    font-family: "Barlow", sans-serif;
    font-weight: 700;
    font-size: 36px;
    line-height: 1.05;
    color: var(--signal-red);
    letter-spacing: 1px;
  }
  .phone {
    position: absolute;
    left: 556px;
    top: 728px;
    width: 584px;
    height: 110px;
  }
  .phone-text {
    font-family: "Barlow Condensed", sans-serif;
    font-weight: 700;
    fill: var(--signal-red);
  }
  .website {
    position: absolute;
    right: 62px;
    top: 846px;
    font-family: "Barlow", sans-serif;
    font-weight: 500;
    font-size: 26px;
    line-height: 1;
    color: var(--muted);
    letter-spacing: 0.5px;
  }
</style>
</head>
<body>
<main class="lease-sign">
  <section class="sign-field">
    <svg class="headline-art" viewBox="0 0 1200 698">
      <polygon class="headline-band" points="0,150 1200,72 1200,345 0,448" fill="var(--signal-red)"/>
      <text class="headline-text" x="600" y="360" font-size="300" text-anchor="middle"
            textLength="1060" lengthAdjust="spacingAndGlyphs"
            transform="rotate(-5 600 260)">FOR LEASE</text>
    </svg>
    <div class="building-plate">your building name</div>
  </section>

  <div class="brand">
    <div class="brand-dot"></div>
    <div class="brand-name">QUILLSTEAD<br>PROPERTIES</div>
  </div>

  <svg class="phone" viewBox="0 0 584 110">
    <text class="phone-text" x="0" y="98" font-size="118" textLength="580" lengthAdjust="spacingAndGlyphs">(816) 555-2719</text>
  </svg>

  <div class="website">www.quillstead-properties.com</div>
</main>
</body>
</html>
```